Redesign our Product Box!

We have a product box for our pet supplement we are looking to redesign. Please use the photoshop file of the current design for the logo/info/dieline and the concept picture of a bag we would like to see included in the box design.

Ideally the background will be the green with white text, but we really want it to be fun and appealing to pet owners so do not be scared to show your vision.

```html
<!DOCTYPE html>
<html lang="en">
<head>
<meta charset="utf-8">
<title>AquaSprout Pet Supplement Box – Dieline</title>
<link href="https://fonts.googleapis.com/css2?family=Source+Sans+3:wght@400;600;700&family=Archivo+Narrow:wght@700&display=swap" rel="stylesheet">
<style>
  :root{
    --box-green:#00a443;
    --ink-white:#ffffff;
    --ink-dark:#1a1a1a;
    --cut-line:#c0392b;
    --fold-line:#3a5fcd;
    --panel-white:#ffffff;
    --swoosh-light:#f4f4f4;
    --swoosh-shade:#d2d2d2;
  }
  html,body{margin:0;width:1200px;height:1200px;overflow:hidden;background:#fff;}
  .dieline{display:block;width:1200px;height:1200px;}
  .dieline text{font-family:"Source Sans 3",sans-serif;}
  .panel{fill:var(--box-green);stroke:var(--cut-line);stroke-width:1;}
  .fold{stroke:var(--fold-line);stroke-width:.8;fill:none;}
  .white-panel{fill:var(--panel-white);}
  .brand-name{fill:var(--ink-white);font-weight:700;font-size:25px;}
  .tagline{fill:var(--ink-white);font-size:13.5px;}
  .copy{fill:var(--ink-white);font-size:9.6px;}
  .copy-bold{fill:var(--ink-white);font-size:11px;font-weight:600;}
  .print-label{fill:var(--ink-dark);font-size:24px;}
  .facts-title{font-family:"Archivo Narrow",sans-serif !important;font-weight:700;font-size:17px;fill:var(--ink-dark);}
  .facts-small{font-size:5.6px;fill:var(--ink-dark);}
  .facts-tiny{font-size:4.2px;fill:#444;}
  .dist-head{font-size:9.5px;font-weight:700;fill:var(--ink-dark);}
  .dist-line{font-size:9px;fill:var(--ink-dark);}
  .facts-rule{stroke:var(--ink-dark);fill:none;}
</style>
</head>
<body>
<svg class="dieline" viewBox="522 1108 790 815" xmlns="http://www.w3.org/2000/svg">
  <defs>
    <linearGradient id="swooshTone" x1="0" y1="0" x2="1" y2="1">
      <stop offset="0" stop-color="var(--swoosh-shade)"/>
      <stop offset="1" stop-color="var(--swoosh-light)"/>
    </linearGradient>
  </defs>

  <!-- top tuck flap and top panel -->
  <path class="panel" d="M587 1185 L587 1170 Q590 1130 617 1123 L752 1123 Q779 1130 781 1170 L781 1185 Z"/>
  <rect class="panel" x="587" y="1185" width="196" height="155"/>
  <text class="brand-name" x="684" y="1257" text-anchor="middle">AquaSprout</text>

  <!-- glue flap -->
  <path class="panel" d="M537 1345 L587 1340 L587 1693 L537 1690 Z"/>

  <!-- side dust flaps (top) -->
  <path class="panel" d="M783 1232 L920 1232 L925 1310 L938 1328 L938 1340 L783 1340 Z"/>
  <path class="panel" d="M1155 1232 L1290 1232 L1290 1322 L1285 1332 L1135 1340 L1135 1328 L1150 1310 Z"/>
  <text class="print-label" x="1037" y="1261" text-anchor="middle">PRINT</text>
  <text class="print-label" x="1030" y="1294" text-anchor="middle">SIDE</text>

  <!-- front panel -->
  <rect class="panel" x="587" y="1340" width="196" height="353"/>
  <text class="brand-name" x="683" y="1403" text-anchor="middle">AquaSprout</text>
  <text class="tagline" x="682" y="1443" text-anchor="middle">Foundational Nutrition</text>
  <text class="tagline" x="682" y="1461" text-anchor="middle">&amp; Super-Antioxidant</text>
  <rect x="598" y="1480" width="183" height="158" rx="60" fill="url(#swooshTone)" role="img" aria-label="White sweeping wing-like swoosh illustration"/>
  <text class="tagline" x="682" y="1507" text-anchor="middle" style="fill:var(--box-green)">For Dogs &amp; Cats</text>
  <text class="copy" x="684" y="1670" text-anchor="middle">15g</text>

  <!-- side panel: directions -->
  <rect class="panel" x="783" y="1340" width="155" height="353"/>
  <g class="copy" text-anchor="middle">
    <text x="861" y="1362">Directions: For dogs &amp; cats</text>
    <text x="861" y="1375">1/16tsp once per day.</text>
    <text x="861" y="1388">Administer orally. To be mixed</text>
    <text x="861" y="1401">into food. 1/16tsp = 1/2 the</text>
    <text x="861" y="1414">included scoop.</text>
    <text x="861" y="1492">Phytoplankton is the foundation of</text>
    <text x="861" y="1505">life, It is the first plant in the entire</text>
    <text x="861" y="1518">food chain.</text>
    <text x="861" y="1544">Phytoplankton is a microscopic</text>
    <text x="861" y="1557">powerhouse. Your pet's body</text>
    <text x="861" y="1570">absorbs billions of phytoplankton</text>
    <text x="861" y="1583">with every serving.</text>
    <text x="861" y="1609">Packed with the building blocks of</text>
    <text x="861" y="1622">life, phytoplankton addresses</text>
    <text x="861" y="1635">multiple aspects of your pet's</text>
    <text x="861" y="1648">health in one simple supplement.</text>
  </g>
  <line x1="806" y1="1436" x2="916" y2="1436" stroke="var(--ink-white)" stroke-width="1"/>
  <text class="copy-bold" x="861" y="1450" text-anchor="middle">Unlock Nature's</text>
  <text class="copy-bold" x="861" y="1465" text-anchor="middle">Nutrient Treasure:</text>

  <!-- back panel: supplement facts -->
  <rect class="panel" x="938" y="1340" width="197" height="353"/>
  <rect class="white-panel" x="941" y="1345" width="191" height="308"/>
  <rect class="facts-rule" x="950" y="1355" width="177" height="92" stroke-width="1.2"/>
  <text class="facts-title" x="1035" y="1372" text-anchor="middle">Supplement Facts</text>
  <line class="facts-rule" x1="950" y1="1378" x2="1127" y2="1378" stroke-width="2"/>
  <text class="facts-small" x="961" y="1389">Serving Size: 1 Scoop/Day</text>
  <text class="facts-small" x="961" y="1395">Servings per Container: 30</text>
  <text class="facts-small" x="1047" y="1395">Amount per Serving</text>
  <text class="facts-small" x="1106" y="1395">%DV</text>
  <line class="facts-rule" x1="950" y1="1402" x2="1127" y2="1402" stroke-width="1.5"/>
  <text class="facts-small" x="961" y="1416">Microalgae Nannochloropsis Gaditana</text>
  <text class="facts-small" x="1083" y="1416">500mg</text>
  <text class="facts-small" x="1112" y="1416">‡</text>
  <line class="facts-rule" x1="950" y1="1428" x2="1127" y2="1428" stroke-width="1.5"/>
  <text class="facts-small" x="961" y="1439">‡ Daily value not established.</text>
  <text class="facts-tiny" x="950" y="1455">These statements have not been evaluated by the Food and Drug Administration.</text>
  <text class="facts-tiny" x="950" y="1461">This product is not intended to diagnose, treat, cure, or prevent any disease.</text>
  <text class="facts-tiny" x="950" y="1474">Store in a cool, dry place.</text>
  <text class="dist-head" x="951" y="1497">Distributed By::</text>
  <text class="dist-line" x="951" y="1509">Tidewell Nutrition Inc.</text>
  <text class="dist-line" x="951" y="1521">42 Harbour Road,</text>
  <text class="dist-line" x="951" y="1533">Fairport, Nova Scotia Canada</text>
  <text class="dist-line" x="951" y="1545">B0X 1A0</text>
  <g class="facts-tiny" style="font-size:5.4px">
    <text x="950" y="1555">Warnings: Check with a qualified healthcare professional before</text>
    <text x="950" y="1562">using this product if you are pregnant, breastfeeding, or taking</text>
    <text x="950" y="1569">blood thinners. You should call your doctor for medical advice</text>
    <text x="950" y="1576">about serious adverse events. To report a serious adverse event</text>
    <text x="950" y="1583">or obtain product information contact: 1 800 555 0190</text>
  </g>
  <text class="copy" x="1037" y="1671" text-anchor="middle" style="font-size:10px">Customer Care: 1 800 555 0190</text>
  <text class="copy" x="1037" y="1684" text-anchor="middle" style="font-size:10px">tidewellnutrition.com</text>

  <!-- side panel: about -->
  <rect class="panel" x="1135" y="1340" width="155" height="353"/>
  <g class="copy" text-anchor="middle">
    <text x="1212" y="1362">Our premium phytoplankton</text>
    <text x="1212" y="1375">powder is a extraordinary</text>
    <text x="1212" y="1388">supplement.  It infuses your pet's</text>
    <text x="1212" y="1401">body with pure, plant-based</text>
    <text x="1212" y="1414">nutrients and potent antioxidants.</text>
    <text x="1212" y="1440">Phytoplankton goes beyond</text>
    <text x="1212" y="1453">ordinary supplements; it's a path</text>
    <text x="1212" y="1466">to optimal health. In just a few</text>
    <text x="1212" y="1479">weeks, your pet will experience a</text>
    <text x="1212" y="1492">feeling of calm and strength, the</text>
    <text x="1212" y="1505">kind of wellness our customers</text>
    <text x="1212" y="1518">often say they've been seeking.</text>
    <text x="1212" y="1544">Join those who have discovered</text>
    <text x="1212" y="1557">the transformative power of</text>
    <text x="1212" y="1570">phytoplankton. See the difference</text>
    <text x="1212" y="1583">for yourself and understand why</text>
    <text x="1212" y="1596">it's not just a supplement, but a</text>
    <text x="1212" y="1609">revolution in pet health and</text>
    <text x="1212" y="1622">vitality.</text>
  </g>

  <!-- bottom flaps -->
  <path class="panel" d="M783 1693 L938 1693 L938 1803 L802 1803 L796 1712 Z"/>
  <path class="panel" d="M1135 1693 L1290 1693 L1290 1708 L1276 1718 L1273 1803 L1135 1803 Z"/>
  <rect class="panel" x="938" y="1693" width="197" height="157"/>
  <text class="copy" x="1037" y="1833" text-anchor="middle" transform="rotate(180 1037 1830)" style="font-size:11px">Exp: 2025/03/Lot No.:1 2222</text>
  <path class="panel" d="M938 1850 L1135 1850 L1135 1865 Q1132 1900 1105 1910 L968 1910 Q941 1900 938 1865 Z"/>

  <!-- fold lines -->
  <g class="fold">
    <line x1="587" y1="1185" x2="781" y2="1185"/>
    <line x1="587" y1="1340" x2="1290" y2="1340"/>
    <line x1="587" y1="1693" x2="1290" y2="1693"/>
    <line x1="587" y1="1340" x2="587" y2="1693"/>
    <line x1="783" y1="1340" x2="783" y2="1693"/>
    <line x1="938" y1="1340" x2="938" y2="1693"/>
    <line x1="1135" y1="1340" x2="1135" y2="1693"/>
    <line x1="938" y1="1850" x2="1135" y2="1850"/>
  </g>
</svg>
</body>
</html>
```